Brisko Sky Park needs a new upscale business card design for our high end aircraft hangar complex

Brisko Sky Park (BSP) is a large, upscale jet hangar complex in the US housing expensive aircraft. We need a new business card design, using our current logo. We will be attending a industry convention and need a card design that will stand out and be remembered by aircraft owners and private pilots.

Target Market(s)

Aircraft pilots or owners looking for a new upscale hangar

Industry/Entity Type

Airport

Contact Information for Business Card

I like to use very heavy card stock, 400#, double sided. Square, no rounded edges please.

Colors
3276b5
0255a3
85abd2

Requirements
Must have
• An expensive, classy design, vivid colors.
Nice to have
• Needs to look very expensive and classy, and have some "pop". Designer must be able to download or copy my current typeface or fonts.
• One card side might be black with the "Logo and Brisko Sky Park Double line image in blue (or try gold, or glossy black), and perhaps have a grayed out "K480 jet silhouette". The other card side would have our contact info, and perhaps the "BSP Logo only". I'd like my contact info 'stacked', not in a paragraph format.
Should not have
• Should not look "too busy". Having a double-sided card will help.

```html
<!DOCTYPE html>
<html lang="en">
<head>
<meta charset="UTF-8">
<title>Brisko Sky Park – Business Card</title>
<link rel="stylesheet" href="https://fonts.googleapis.com/css2?family=Roboto:wght@400;500;700&display=swap">
<style>
  :root {
    --page-bg: #e9e7e3;
    --card-white: #f7f7f7;
    --sky-light: #4aaed8;
    --sky-mid: #3276b5;
    --sky-deep: #0255a3;
    --sky-pale: #85abd2;
    --card-dark: #3a3b3e;
    --card-dark-arc: #333437;
    --jet-grey: #2d2e31;
    --text-light: #ffffff;
  }
  * { margin: 0; padding: 0; box-sizing: border-box; }
  html, body { width: 1200px; height: 1023px; overflow: hidden; }
  body {
    background: var(--page-bg);
    font-family: "Roboto", Arial, sans-serif;
    position: relative;
  }
  .card {
    position: absolute;
    left: 220px;
    width: 760px;
    height: 434px;
    overflow: hidden;
    box-shadow: 0 10px 28px rgba(0,0,0,0.22);
  }
  .card-front { top: 40px; background: var(--card-white); }
  .card-back { top: 534px; background: var(--card-dark); }

  .front-shape { position: absolute; inset: 0; width: 100%; height: 100%; }

  .front-brand {
    position: absolute;
    left: 62px;
    top: 262px;
    font-weight: 700;
    font-size: 76px;
    letter-spacing: 4px;
    color: var(--sky-deep);
    display: flex;
    align-items: center;
    gap: 16px;
  }
  .brand-dot {
    width: 18px; height: 18px; border-radius: 50%;
    background: var(--sky-deep);
  }

  .contact {
    position: absolute;
    right: 56px;
    top: 52px;
    width: 300px;
    color: var(--text-light);
    text-align: right;
  }
  .contact-name { font-size: 34px; font-weight: 500; line-height: 1.1; }
  .contact-title { font-size: 17px; font-weight: 400; margin-top: 2px; }
  .contact-rule {
    height: 1px; margin: 14px 0 18px;
    background: linear-gradient(to left, rgba(255,255,255,0.9), rgba(255,255,255,0));
  }
  .contact-list { list-style: none; }
  .contact-list li {
    display: flex; justify-content: flex-end; align-items: center;
    gap: 12px; font-size: 18px; line-height: 32px;
  }
  .contact-list svg { width: 16px; height: 16px; flex: none; }

  .back-arc { position: absolute; inset: 0; width: 100%; height: 100%; }
  .back-brand {
    position: absolute;
    left: 0; right: 0; top: 120px;
    text-align: center;
    font-weight: 700;
    font-size: 120px;
    letter-spacing: 10px;
    color: var(--sky-deep);
  }
  .back-brand span { color: #1371c9; }
  .jet-silhouette {
    position: absolute;
    right: 40px; bottom: 60px;
    width: 230px; height: 90px;
    background: var(--jet-grey);
    border-radius: 45px;
    opacity: 0.8;
  }
</style>
</head>
<body>

<section class="card card-front" aria-label="Card front">
  <svg class="front-shape" viewBox="0 0 760 434" preserveAspectRatio="none" aria-hidden="true">
    <defs>
      <radialGradient id="skyFill" cx="0.55" cy="0.35" r="0.75">
        <stop offset="0" stop-color="#4aaed8"/>
        <stop offset="0.6" stop-color="#3a8fc8"/>
        <stop offset="1" stop-color="#3276b5"/>
      </radialGradient>
    </defs>
    <rect width="760" height="434" fill="url(#skyFill)"/>
    <path d="M0 150 L120 150 C230 150 290 210 290 275 C290 330 255 360 210 372 C400 372 620 330 760 260 L760 434 L0 434 Z" fill="#f7f7f7"/>
  </svg>

  <div class="front-brand"><span class="brand-dot"></span>BSP</div>

  <div class="contact">
    <div class="contact-name">Your Name</div>
    <div class="contact-title">Title</div>
    <div class="contact-rule"></div>
    <ul class="contact-list">
      <li>88-123-54321
        <svg viewBox="0 0 16 16"><path d="M4 1 L6.5 4.5 L5 6 C6 8.5 7.5 10 10 11 L11.5 9.5 L15 12 L13 15 C7 14.5 1.5 9 1 3 Z" fill="#fff"/></svg>
      </li>
      <li>info@yourweb.com
        <svg viewBox="0 0 16 16"><rect x="1" y="3" width="14" height="10" fill="none" stroke="#fff" stroke-width="1.4"/><path d="M1 3 L8 9 L15 3" fill="none" stroke="#fff" stroke-width="1.4"/></svg>
      </li>
      <li>www.yourweb.com
        <svg viewBox="0 0 16 16"><circle cx="8" cy="8" r="6.5" fill="none" stroke="#fff" stroke-width="1.4"/><ellipse cx="8" cy="8" rx="2.8" ry="6.5" fill="none" stroke="#fff" stroke-width="1.2"/><path d="M1.5 8 H14.5 M2.5 5 H13.5 M2.5 11 H13.5" stroke="#fff" stroke-width="1.1"/></svg>
      </li>
    </ul>
  </div>
</section>

<section class="card card-back" aria-label="Card back">
  <svg class="back-arc" viewBox="0 0 760 434" preserveAspectRatio="none" aria-hidden="true">
    <path d="M0 330 C200 260 520 250 760 300 L760 434 L0 434 Z" fill="#333437"/>
  </svg>
  <div class="back-brand">BSP</div>
  <div class="jet-silhouette" role="img" aria-label="Faint grey silhouette of a K480 business jet"></div>
</section>

</body>
</html>
```